Vision / Mission Poster Required

We are looking to display our company Vision / Mission / Values on a poster. This will be displayed in the head office and other site offices.

The document needs to look professional however still be fun, eye catching and easy to read. It will be predominantly displayed in A3 format.

The design needs to use our company Logo which is attached along with the Text to display on the poster. I have put some additional text on the doc that you can include if it suits the layout but is not essential.

Target Market(s)

Staff, Corporate Visitors

Industry/Entity Type

Electric Company

Font styles to use
Sans Serif

Colors

Designer to choose colors to be used in the design.

Requirements
Must have
• Incorporate Logo
• Professional Look
• Attention grabbing
• Easy to Read
Should not have
• Lightning Bolts
• Pictures of random people/Things

```html
<!DOCTYPE html>
<html lang="en">
<head>
<meta charset="utf-8">
<title>Kestrova – Vision, Mission &amp; Values</title>
<link href="https://fonts.googleapis.com/css2?family=Montserrat:wght@500;700;800&family=Questrial&display=swap" rel="stylesheet">
<style>
  :root {
    --steel-light: #d9dadc;
    --steel-mid: #b9bbbe;
    --steel-dark: #a4a6a9;
    --band: #e8e9ea;
    --navy: #0f3f78;
    --orange: #f15a24;
    --red: #c1272d;
    --white: #ffffff;
  }
  html, body {
    margin: 0;
    padding: 0;
    overflow: hidden;
    background: #ffffff;
  }
  .poster {
    position: relative;
    width: 854px;
    height: 1200px;
    overflow: hidden;
    background: linear-gradient(160deg, var(--steel-light) 0%, var(--steel-mid) 45%, var(--steel-light) 70%, var(--steel-dark) 100%);
    font-family: "Montserrat", Arial, sans-serif;
    color: var(--white);
  }
  .brand-panel {
    position: absolute;
    left: 0; top: 30px;
    width: 750px; height: 174px;
    background: var(--band);
    opacity: 0.92;
    display: flex;
    align-items: center;
    gap: 30px;
    padding-left: 62px;
    box-sizing: border-box;
  }
  .brand-dot {
    width: 110px; height: 110px;
    border-radius: 50%;
    background: var(--orange);
    flex: none;
  }
  .brand-name {
    font-family: "Montserrat", Arial, sans-serif;
    font-weight: 800;
    font-size: 84px;
    letter-spacing: 1px;
    color: var(--navy);
  }
  .section-band {
    position: absolute;
    left: 0;
    width: 432px; height: 57px;
    background: var(--band);
    opacity: 0.95;
  }
  .section-title {
    position: absolute;
    left: 0;
    width: 426px;
    margin: 0;
    text-align: center;
    font-family: "Questrial", Arial, sans-serif;
    font-weight: 400;
    font-size: 48px;
    line-height: 57px;
    color: var(--orange);
    letter-spacing: 1px;
  }
  .vision-statement {
    position: absolute;
    left: 34px; top: 310px;
    margin: 0;
    font-size: 24.8px;
    line-height: 30px;
    font-weight: 700;
    white-space: nowrap;
    text-shadow: 0 1px 2px rgba(0,0,0,.25);
  }
  .tagline {
    position: absolute;
    left: 63px; top: 360px;
    margin: 0;
    font-size: 23px;
    line-height: 28px;
    font-weight: 700;
    white-space: nowrap;
    color: var(--red);
  }
  .switchboard-photo {
    position: absolute;
    left: 615px; top: 351px;
    width: 239px; height: 178px;
    background: linear-gradient(100deg, #3a3b3d 0%, #8a8c8e 28%, #e86a1c 45%, #f07a22 75%, #c4561a 100%);
  }
  .heading {
    position: absolute;
    margin: 0;
    font-weight: 700;
    color: var(--navy);
    white-space: nowrap;
  }
  .mission-heading { font-size: 24px; line-height: 29px; left: 24px; }
  .value-heading { font-size: 24.5px; line-height: 30px; }
  .copy {
    position: absolute;
    margin: 0;
    font-weight: 700;
    white-space: nowrap;
    text-shadow: 0 1px 2px rgba(0,0,0,.25);
  }
  .mission-copy { font-size: 19.8px; line-height: 29.5px; left: 24px; }
  .value-copy { font-size: 15px; line-height: 23px; }
</style>
</head>
<body>
<main class="poster">
  <header class="brand-panel">
    <span class="brand-dot"></span>
    <span class="brand-name">KESTROVA</span>
  </header>

  <div class="section-band" style="top:235px"></div>
  <h2 class="section-title" style="top:235px">VISION</h2>
  <p class="vision-statement">To be Perth’s Premier Provider of Electrical Service Solutions</p>
  <p class="tagline">DYNAMIC RESULTS - PROVEN REPUTATION</p>
  <div class="switchboard-photo" role="img" aria-label="Photo of orange industrial electrical switchboard cabinets"></div>

  <div class="section-band" style="top:418px"></div>
  <h2 class="section-title" style="top:418px">MISSION</h2>

  <h3 class="heading mission-heading" style="top:503px">DELIVER GROWTH &amp; VALUE</h3>
  <p class="copy mission-copy" style="top:529px">Maintaining a Market Presence | Leveraging our Technical<br>Resources | Networking &amp; Developing Stakeholder Relationships.</p>

  <h3 class="heading mission-heading" style="top:595px">REMAIN PROFITABLE</h3>
  <p class="copy mission-copy" style="top:623px">Increasing Revenue | Optimizing Capacity Utilization | Maintaining Expenses.</p>

  <h3 class="heading mission-heading" style="top:663px">BE SUSTAINABLE</h3>
  <p class="copy mission-copy" style="top:689px;left:17px">Improving Internal Efficiency | Diversifying our Income Sources | Implementing<br>Social &amp; Environmental Improvement Initiatives.</p>

  <div class="section-band" style="top:771px"></div>
  <h2 class="section-title" style="top:771px">VALUES</h2>

  <h3 class="heading value-heading" style="top:836px;left:35px">HONESTY &amp; INTEGRITY</h3>
  <p class="copy value-copy" style="top:860px;left:36px">Customers, Contractors &amp; Suppliers will be able to count on Kestrova personnel to deal<br>Straightforwardly and adhere to the Strictest Moral &amp; Ethical codes of Conduct.</p>

  <h3 class="heading value-heading" style="top:908px;left:65px">SAFETY &amp; RESPONSIBILITY</h3>
  <p class="copy value-copy" style="top:935px;left:65px">Kestrova is Committed to Constantly Improving Safety practices at project job sites<br>and within the electrical service industry as a Whole.</p>

  <h3 class="heading value-heading" style="top:977px;left:102px">COMMITMENT TO QUALITY</h3>
  <p class="copy value-copy" style="top:1001px;left:102px">Customers &amp; Stakeholders will be able to count on Kestrova's workmanship being<br>among the Best in the Industry.</p>

  <h3 class="heading value-heading" style="top:1041px;left:138px">INNOVATION &amp; TECHNOLOGY</h3>
  <p class="copy value-copy" style="top:1068px;left:138px">Customers can Rely on us to apply the Latest proven technologies on their projects,<br>and to be on the ground floor of industry Standards for New &amp; Emerging markets.</p>

  <h3 class="heading value-heading" style="top:1110px;left:174px">KNOWLEDGABLE &amp; VALUED EMPLOYEES</h3>
  <p class="copy value-copy" style="top:1138px;left:174px">Kestrova Recognizes that its Greatest Asset is its People. We pledge to treat each<br>Employee with Integrity, dealing Honestly with All.</p>
</main>
</body>
</html>
```